Brookvale Services telephone book advert

Design a tellwick directory telephone book advertisement. Attached is a current version of the brookvale services advert. Please use the same information as detailed on the existing advert but arty!. Overall size should be 130 mm by 91 mm portrait using one of the specified colours plus black. Any background should be opaque (not white). and delivered in the formats as specified.

```html
<!DOCTYPE html>
<html lang="en">
<head>
<meta charset="utf-8">
<title>Brookvale Services Limited – Directory Advert</title>
<link href="https://fonts.googleapis.com/css2?family=Roboto:wght@400;500;700;900&family=Roboto+Condensed:wght@400;700&display=swap" rel="stylesheet">
<style>
  :root {
    --navy: #28308c;
    --navy-deep: #1b2160;
    --navy-mid: #2a3490;
    --yellow: #fde21a;
    --paper: #eef0f3;
    --paper-light: #f8f9fb;
    --ink: #1d1d22;
    --white: #ffffff;
  }
  html, body { margin: 0; padding: 0; overflow: hidden; background: #d9dbe0; }
  .advert {
    position: relative;
    width: 839px;
    height: 1200px;
    overflow: hidden;
    background: linear-gradient(180deg, var(--paper-light) 0%, var(--paper) 100%);
    font-family: "Roboto Condensed", "Arial Narrow", sans-serif;
    color: var(--ink);
  }
  .hero-backdrop {
    position: absolute; left: 0; top: 0; width: 839px; height: 656px;
    background: linear-gradient(135deg, #2b3594 0%, #1f2870 45%, #182057 100%);
  }
  .hero-shapes { position: absolute; left: 0; top: 0; }
  .headline {
    position: absolute; left: 36px; top: 44px; margin: 0;
    font-family: "Roboto", Arial, sans-serif; color: var(--white);
    text-shadow: 0 3px 6px rgba(0,0,0,.35);
  }
  .headline .line-big { display: block; font-weight: 700; font-size: 76px; line-height: 84px; letter-spacing: -1px; }
  .headline .line-small { display: block; font-weight: 400; font-size: 58px; line-height: 68px; margin-top: 4px; }
  .call-band {
    position: absolute; left: 38px; top: 338px; color: var(--ink);
  }
  .call-band .lead { font-family: "Roboto", Arial, sans-serif; font-size: 34px; line-height: 38px; font-weight: 400; }
  .call-band .phone {
    display: block; margin-top: 2px; margin-left: -8px;
    font-family: "Roboto Condensed", sans-serif; font-weight: 700;
    font-size: 112px; line-height: 112px; color: var(--navy); letter-spacing: -1px;
  }
  .surveys-heading {
    position: absolute; left: 36px; top: 574px; margin: 0;
    font-family: "Roboto", Arial, sans-serif; font-weight: 700; font-size: 48px;
    color: var(--white); letter-spacing: -0.5px;
  }
  .services-card {
    position: absolute; left: 38px; top: 712px; width: 395px; height: 438px;
    border: 2px solid var(--yellow); border-radius: 14px; background: var(--white);
    box-sizing: border-box;
  }
  .services-tab {
    position: absolute; left: 78px; top: 692px; width: 318px; height: 40px;
    background: var(--yellow); color: var(--navy);
    font-family: "Roboto Condensed", sans-serif; font-weight: 700; font-size: 32px;
    line-height: 40px; text-align: center;
    clip-path: polygon(4% 0, 96% 0, 100% 100%, 0 100%);
  }
  .services-list {
    position: absolute; left: 54px; top: 744px; width: 370px; margin: 0; padding: 0;
    list-style: none; font-size: 33px; line-height: 37px;
  }
  .services-list li { position: relative; padding-left: 27px; margin-bottom: 17px; }
  .services-list li::before {
    content: ""; position: absolute; left: 2px; top: 15px; width: 11px; height: 11px;
    border-radius: 50%; background: var(--navy);
  }
  .contact {
    position: absolute; left: 470px; top: 766px; font-size: 30px; line-height: 36px;
  }
  .contact .role { display: block; }
  .contact .name {
    display: block; margin-top: 6px; margin-bottom: 34px;
    font-weight: 700; font-size: 47px; line-height: 52px; color: var(--navy);
  }
  .contact .highlight { font-weight: 700; color: var(--navy); }
  .contact address { font-style: normal; margin-top: 20px; }
  .footer-rule { position: absolute; left: 0; top: 1186px; width: 839px; height: 14px; background: var(--navy); }
</style>
</head>
<body>
<div class="advert">
  <div class="hero-backdrop" role="img" aria-label="Dark blue toned photograph of drain grates and paving"></div>

  <svg class="hero-shapes" width="839" height="740" viewBox="0 0 839 740" aria-hidden="false">
    <defs>
      <linearGradient id="worksite" x1="0" y1="0" x2="1" y2="1">
        <stop offset="0" stop-color="#8c7a68"/>
        <stop offset="0.5" stop-color="#6e6358"/>
        <stop offset="1" stop-color="#4a4640"/>
      </linearGradient>
      <radialGradient id="spray" cx="0.5" cy="0.5" r="0.6">
        <stop offset="0" stop-color="#e8eaec"/>
        <stop offset="1" stop-color="#a9acae"/>
      </radialGradient>
    </defs>
    <polygon points="0,310 492,310 462,528 0,528" fill="var(--yellow)"/>
    <polygon points="504,0 839,0 839,556 426,556" fill="url(#worksite)"
             role="img" aria-label="Photograph of a worker rodding an open drain chamber beside a yellow pipe"/>
    <line x1="504" y1="0" x2="426" y2="556" stroke="var(--white)" stroke-width="4"/>
    <rect x="0" y="556" width="839" height="100" fill="var(--navy-deep)" opacity="0.85"/>
    <circle cx="700" cy="612" r="114" fill="var(--yellow)"/>
    <circle cx="700" cy="612" r="107" fill="url(#spray)"
            role="img" aria-label="Close-up photograph of a high pressure water jet nozzle spraying paving"/>
  </svg>

  <h1 class="headline">
    <span class="line-big">BROOKVALE</span>
    <span class="line-big">SERVICES</span>
    <span class="line-small">LIMITED</span>
  </h1>

  <div class="call-band">
    <div class="lead">For local drainage<br>expertise call</div>
    <span class="phone">318-624</span>
  </div>

  <h2 class="surveys-heading">Home Buyers Surveys</h2>

  <div class="services-card"></div>
  <div class="services-tab">Our Core Services</div>
  <ul class="services-list">
    <li>Unblocking and high pressure cleaning</li>
    <li>Jetting, de-scaling and root cutting</li>
    <li>Modern CCTV, condition report</li>
    <li>Structural re-lining of damaged and leaky drains</li>
  </ul>

  <div class="contact">
    <span class="role">Contract Manager</span>
    <span class="name">Martin Coldwell</span>
    <div>Email: <span class="highlight">office@brookvale.gg</span><br>
      for more information,<br>
      visit <span class="highlight">www.brookvale.gg</span></div>
    <address>Varclin Lane,<br>St. Peter Port,<br>Guernsey GY1 3RT</address>
  </div>

  <div class="footer-rule"></div>
</div>
</body>
</html>
```